依頼詳細
珪藻土バスマットを販売するにあたり、店舗にチラシを設置しようと思います。そのチラシ制作をお願いします。同種製品が多いので明るくおしゃれでわかりやすいデザインを望んでいます。
以前使用していたデモチラシがあるので内容は同じでデザインをかっこよくしてほしいです。
記載項目
キャッチコピー、製品名、特徴、製品写真
※以前使っていたもののデモチラシがあるので基本的に文言などはそちらを参照してください。デモにある文言は必須で入れてください。その他に必要なものがあれば提案で掲載していただいたOKです。
サイズ
A4
ページ数
片面
希望イメージ
シンプル 複雑
単色 カラフル
暗い 明るい
日常 高級
遊び心 厳粛
未来的 伝統的
女性的 男性的
希望する色
納品ファイル
• イラストレーター形式 (.ai)
補足説明
イラストレーターで元データとアウトラインデータを下さい。
関連書類の添付忘れを追加しました。
■ 選んだ理由

関係者の多数決で、メインターゲットとなる女性に人気があったため選ばせていただきました。

■ 提案者全員のお礼・コメント

みなさん非常に素敵なデザインで本当に迷いました。せっかく作っていただいてもったいないのですが、今回は関係者の多数決で1点に絞らせていただきました。

提案くださった皆様ありがとうございました!

```html
<!DOCTYPE html>
<html lang="ja">
<head>
<meta charset="UTF-8">
<title>爽やかサラリマット</title>
<link href="https://fonts.googleapis.com/css2?family=M+PLUS+Rounded+1c:wght@500;700;800&display=swap" rel="stylesheet">
<style>
  :root{
    --sky:#cfe6f6;
    --sky-deep:#9fcdee;
    --blue:#2d8ad6;
    --pink:#e7569a;
    --white:#ffffff;
    --mat:#e9e7e2;
    --pastel-pink:#f7b9d3;
    --pastel-yellow:#f9e08a;
    --pastel-green:#b6e2a1;
    --pastel-purple:#cdb8ef;
    --pastel-orange:#f8c48e;
    --pink-deep:#d9488a;
    --yellow-deep:#d19a12;
    --green-deep:#4e9d35;
    --purple-deep:#7d5cc4;
  }
  *{margin:0;padding:0;box-sizing:border-box}
  html,body{width:849px;height:1200px;overflow:hidden;background:var(--white)}
  body{font-family:"M PLUS Rounded 1c",sans-serif;color:var(--blue)}
  .flyer{position:relative;width:849px;height:1200px;overflow:hidden;
    background:linear-gradient(180deg,var(--sky) 0%,#e4f1fa 50%,#eef6fc 75%,var(--sky) 100%)}
  .drops-area{position:absolute;left:0;top:0;width:849px;height:290px;
    background:linear-gradient(180deg,#a9d4f1,var(--sky))}
  .origin{position:absolute;left:16px;top:12px;padding:2px 6px;border:2px solid var(--blue);
    background:var(--white);font-size:14px;font-weight:700;color:var(--blue)}
  .subtitle{position:absolute;left:0;right:0;top:42px;text-align:center;
    font-size:25px;font-weight:700;color:var(--pink);
    -webkit-text-stroke:4px var(--white);paint-order:stroke fill}
  .subtitle span{border-bottom:3px dotted var(--pink);padding-bottom:3px}
  .title{position:absolute;left:0;right:0;top:130px;text-align:center;font-size:80px;
    font-weight:800;color:var(--blue);letter-spacing:4px;line-height:1;
    -webkit-text-stroke:10px var(--white);paint-order:stroke fill}
  .stage{position:absolute;left:0;top:290px;width:849px;height:300px;
    background:radial-gradient(ellipse at center,#ffffff 50%,#e9f4fc 100%)}
  .product{position:absolute;left:297px;top:290px;width:255px;height:180px;border-radius:16px;
    background:linear-gradient(140deg,#f5f4f0,var(--mat));box-shadow:0 10px 24px rgba(40,90,140,.18)}
  .scene{position:absolute;left:0;top:580px;width:849px;height:355px;
    background:linear-gradient(160deg,#f6f5f2 0%,#e3e1dc 60%,#d6d4cf 100%)}
  .bubble{position:absolute;border-radius:50%;display:flex;align-items:center;justify-content:center;
    font-weight:800;color:var(--white);text-align:center;line-height:1.1;
    paint-order:stroke fill;box-shadow:inset -8px -10px 20px rgba(255,255,255,.45)}
  .b-dry{left:40px;top:305px;width:125px;height:125px;background:var(--pastel-pink);font-size:32px;-webkit-text-stroke:5px var(--pink-deep)}
  .b-odor{left:670px;top:292px;width:125px;height:125px;background:var(--pastel-green);font-size:32px;-webkit-text-stroke:5px var(--green-deep)}
  .b-mold{left:65px;top:470px;width:125px;height:125px;background:var(--pastel-yellow);font-size:29px;-webkit-text-stroke:5px var(--yellow-deep)}
  .b-natural{left:668px;top:500px;width:130px;height:130px;background:var(--pastel-purple);font-size:29px;-webkit-text-stroke:5px var(--purple-deep)}
  .dot{position:absolute;border-radius:50%;opacity:.85}
  .care{position:absolute;right:45px;top:655px;text-align:right;font-size:27px;font-weight:800;
    color:var(--blue);line-height:1.35;-webkit-text-stroke:5px var(--white);paint-order:stroke fill}
  .absorb{position:absolute;left:28px;top:960px;width:120px;height:150px}
  .absorb-text{position:absolute;left:28px;top:1035px;width:120px;text-align:center;
    font-size:22px;font-weight:800;color:var(--white);line-height:1.2}
  .step{position:absolute;border-radius:50%;border:5px solid var(--white);
    box-shadow:0 6px 16px rgba(40,90,140,.2)}
  .step-1{left:215px;top:1075px;width:140px;height:140px;background:linear-gradient(135deg,#bfc3c8,#8e949b)}
  .step-2{left:370px;top:1050px;width:190px;height:190px;background:linear-gradient(135deg,#d2d5d8,#a7acb1)}
  .step-3{left:545px;top:905px;width:250px;height:250px;background:linear-gradient(135deg,#f4f4f2,#d9dbdd)}
  .num{position:absolute;width:34px;height:34px;border-radius:50%;background:var(--sky-deep);
    border:2px solid var(--white);color:var(--white);font-size:18px;font-weight:800;
    display:flex;align-items:center;justify-content:center}
</style>
</head>
<body>
<div class="flyer">
  <div class="drops-area" role="img" aria-label="水滴の背景パターン"></div>
  <div class="origin">日本製</div>
  <p class="subtitle"><span>バーミキュライトと珪藻土を配合した多機能素材！</span></p>
  <h1 class="title">爽やかサラリマット</h1>

  <div class="stage"></div>
  <div class="scene" role="img" aria-label="バスマットに素足で乗る写真"></div>
  <div class="product" role="img" aria-label="珪藻土バスマットの製品写真"></div>

  <div class="dot" style="left:215px;top:300px;width:26px;height:26px;background:var(--pastel-orange)"></div>
  <div class="dot" style="left:600px;top:420px;width:30px;height:30px;background:var(--pastel-yellow)"></div>
  <div class="dot" style="left:215px;top:440px;width:22px;height:22px;background:var(--pastel-green)"></div>
  <div class="dot" style="left:800px;top:430px;width:28px;height:28px;background:var(--pastel-pink)"></div>
  <div class="dot" style="left:15px;top:450px;width:30px;height:30px;background:var(--pastel-purple)"></div>
  <div class="dot" style="left:605px;top:300px;width:20px;height:20px;background:var(--pastel-pink)"></div>

  <div class="bubble b-dry">速乾</div>
  <div class="bubble b-odor">消臭</div>
  <div class="bubble b-mold">防カビ</div>
  <div class="bubble b-natural">天然<br>素材</div>

  <p class="care">お手入れカンタン！<br>何回使っても<br>すぐにサラサラ！</p>

  <svg class="absorb" viewBox="0 0 120 150" aria-hidden="true">
    <path d="M60 4 C76 44 112 74 112 102 A52 48 0 0 1 8 102 C8 74 44 44 60 4 Z" fill="#5aaee6"/>
  </svg>
  <p class="absorb-text">抜群の<br>吸水力</p>

  <svg width="849" height="1200" style="position:absolute;left:0;top:0" aria-hidden="true">
    <path d="M330 1110 L385 1100" stroke="#9fcdee" stroke-width="4" fill="none"/>
    <path d="M535 1080 L575 1060" stroke="#9fcdee" stroke-width="4" fill="none"/>
  </svg>
  <div class="step step-1" role="img" aria-label="水を含んだ直後のマット表面の写真"></div>
  <div class="step step-2" role="img" aria-label="水が吸収されていくマット表面の写真"></div>
  <div class="step step-3" role="img" aria-label="乾いてサラサラになったマット表面の写真"></div>
  <div class="num" style="left:262px;top:1120px">1</div>
  <div class="num" style="left:435px;top:1120px">2</div>
  <div class="num" style="left:635px;top:1100px">3</div>
</div>
</body>
</html>
```